Professional Facebook Banner, Business Cards, Door Hang Tags, Service Flyer for Pest Control Company

There are really 4 things I need designed but Brief Hive doesn't have them to package together. I am needing to get a Professional Facebook Banner, Business Cards, Door Hang Tags, and Service Flyer for a Pest Control Company. I already have a logo that I will attach to the project along with content a for each one of these tasks. Please see document attached labeled All Design Content & Flyer Content.
Pest Control

```html
<!DOCTYPE html>
<html lang="en">
<head>
<meta charset="utf-8">
<title>Citrus Grove Pest Control – Print & Social Set</title>
<link rel="stylesheet" href="https://fonts.googleapis.com/css2?family=Archivo+Black&family=Exo+2:wght@300;400;700&family=Oswald:wght@500;700&display=swap">
<style>
  :root{
    --sheet:#c6c6c6;
    --ink:#0b0b0b;
    --orange:#ee6a24;
    --white:#ffffff;
    --paper:#ffffff;
    --bronze:#d39a44;
    --bronze-dark:#b97f2f;
    --silver:#dcd9d6;
    --silver-dark:#b9b5b1;
    --gold:#e6bb2b;
    --gold-dark:#c99d16;
    --label:#222222;
  }
  *{box-sizing:border-box;margin:0;padding:0}
  html,body{width:1200px;height:1200px;overflow:hidden;background:var(--sheet)}
  body{position:relative;font-family:"Exo 2",sans-serif;color:var(--ink)}
  .sprites{position:absolute;width:0;height:0}

  .piece-label{position:absolute;font:400 12.5px/1 "Exo 2",sans-serif;color:var(--label);text-align:center;letter-spacing:.2px}
  .piece{position:absolute;overflow:hidden}
  .dark{background:var(--ink);color:var(--white)}

  /* brand lockup */
  .brand{position:absolute;left:0;right:0;display:flex;align-items:center;justify-content:center;gap:6px;color:var(--orange);font-family:"Oswald",sans-serif;font-weight:700}
  .brand-dot{border-radius:50%;background:var(--orange);flex:none}
  .brand-name{text-align:center;line-height:1}
  .brand-name .line-main{display:block;letter-spacing:1px}
  .brand-name .line-sub{display:block;letter-spacing:.55em;margin-right:-.55em}

  /* door hanger */
  .hanger{top:132px;width:272px;height:633px}
  .hanger-front{left:29px}
  .hanger-back{left:323px}
  .hanger .brand{top:18px}
  .hanger .brand-dot{width:12px;height:12px}
  .hanger .line-main{font-size:19px}
  .hanger .line-sub{font-size:7px;margin-top:3px}
  .hanger-hole{position:absolute;left:0;top:56px}
  .headline{position:absolute;left:0;right:0;text-align:center;font-family:"Archivo Black",sans-serif;line-height:1;white-space:nowrap}
  .headline .hl-orange{color:var(--orange)}
  .headline .hl-white{color:var(--white)}
  .hanger-front .headline{top:148px;font-size:51px;line-height:59px}
  .callout{position:absolute}
  .callout svg{position:absolute;left:0;top:0}
  .callout-text{position:absolute;left:0;right:0;text-align:center;color:var(--orange);white-space:nowrap}
  .offer-amount{font:700 48px/1 "Oswald",sans-serif;letter-spacing:-1px}
  .offer-amount small{font-size:24px;letter-spacing:0}
  .offer-terms{font:300 10.5px/1.15 "Exo 2",sans-serif}
  .photo{position:absolute;background:linear-gradient(160deg,#5a5a5a 0%,#2a2a2a 55%,#e9782e 56%,#c85a1c 80%,#2f2f2f 100%)}
  .phone-band{position:absolute;left:35px;width:200px;background:var(--orange);color:var(--ink);display:flex;align-items:center;justify-content:center;gap:6px;font:700 18px/1 "Oswald",sans-serif}
  .cta-band{position:absolute;left:35px;width:200px;background:var(--white);color:var(--ink);text-align:center;font:500 13px/27px "Oswald",sans-serif;letter-spacing:.2px}
  .about{position:absolute;left:36px;right:36px;top:152px;text-align:center;color:var(--orange);font:300 9.2px/13px "Exo 2",sans-serif}
  .about p+p{margin-top:13px}
  .section-title{position:absolute;left:0;right:0;text-align:center;color:var(--orange);font:700 20px/1 "Oswald",sans-serif;letter-spacing:.5px}
  .icon-row{position:absolute;display:flex}
  .pest-icon{border-radius:50%;background:var(--white);display:flex;align-items:center;justify-content:center;box-shadow:0 2px 0 #bdbdbd;flex:none}
  .pest-icon.is-active{background:var(--white);box-shadow:0 0 0 3px var(--orange),0 2px 0 #9d4718}
  .pest-icon svg{width:60%;height:60%}
  .web-band{position:absolute;background:var(--orange);color:var(--ink);text-align:center;font:700 13px/1 "Oswald",sans-serif;display:flex;align-items:center;justify-content:center}

  /* flyer */
  .flyer{left:615px;top:47px;width:556px;height:718px;background:var(--paper);border:1px solid #999}
  .flyer .brand{top:48px}
  .flyer .brand-dot{width:16px;height:16px}
  .flyer .line-main{font-size:26px}
  .flyer .line-sub{font-size:9px;margin-top:4px;color:var(--orange)}
  .flyer-copy{position:absolute;left:62px;right:42px;top:131px;font:300 8.7px/11.8px "Exo 2",sans-serif;color:var(--ink)}
  .flyer-copy p+p{margin-top:11.8px}
  .flyer-copy strong{color:var(--orange);font-weight:700}
  .tiers{position:absolute;left:0;top:0}
  .tier-name{font:700 16px/20px "Exo 2",sans-serif;fill:var(--ink)}
  .tier-feature{font:400 6.6px "Exo 2",sans-serif;fill:#3a3a3a}
  .tier-price{font:700 18px "Exo 2",sans-serif;fill:var(--ink)}
  .tier-extra{font:700 7.4px "Exo 2",sans-serif;fill:var(--ink)}
  .flyer-note{position:absolute;left:60px;right:60px;top:667px;text-align:center;font:400 6.6px/10px "Exo 2",sans-serif;color:#333}
  .flyer-note strong{font-weight:700}

  /* business cards */
  .card{left:47px;width:254px;height:145px}
  .card-front{top:833px}
  .card-back{top:1026px}
  .card .brand-dot{width:9px;height:9px}
  .card-front .brand{top:28px}
  .card-front .line-main{font-size:17px}
  .card-front .line-sub{font-size:6.5px;margin-top:3px}
  .card-phone{position:absolute;left:121px;top:97px;width:133px;height:17px;background:var(--white);clip-path:polygon(9px 0,100% 0,100% 100%,0 100%);display:flex;align-items:center;justify-content:center;gap:4px;font:700 11px/1 "Oswald",sans-serif;color:var(--ink)}
  .card-owner{position:absolute;left:0;top:114px;width:120px;height:15px;background:var(--orange);clip-path:polygon(0 0,100% 0,calc(100% - 8px) 100%,0 100%);padding-left:14px;font:italic 700 6.4px/15px "Oswald",sans-serif;color:var(--ink);letter-spacing:.3px}
  .card-email{position:absolute;left:126px;top:114px;width:128px;text-align:center;font:700 6.4px/15px "Oswald",sans-serif;color:var(--orange);letter-spacing:.3px}
  .card-tab{position:absolute;left:84px;width:85px;background:var(--orange);color:var(--ink);text-align:center;font:500 6px/16px "Oswald",sans-serif}
  .card-back .brand{top:40px}
  .card-back .line-main{font-size:12px}
  .card-back .line-sub{font-size:4.6px;margin-top:2px}
  .card-back .icon-row{left:23px;top:71px;gap:5.5px}
  .card-back .pest-icon{width:25px;height:25px}
  .icon-caption{position:absolute;top:101px;width:31px;text-align:center;font:500 3.8px/1.2 "Oswald",sans-serif;color:var(--orange)}

  /* social banner */
  .banner{left:345px;top:808px;width:826px;height:363px}
  .banner .brand{left:0;right:auto;width:450px;top:22px}
  .banner .brand-dot{width:22px;height:22px}
  .banner .line-main{font-size:46px}
  .banner .line-sub{font-size:13px;margin-top:6px}
  .banner .headline{left:38px;right:auto;width:372px;top:120px;font:700 66px/1 "Oswald",sans-serif;letter-spacing:.5px}
  .banner-phone{position:absolute;left:40px;top:196px;width:366px;height:64px;background:var(--orange);border-radius:4px 14px 14px 4px;display:flex;align-items:center;justify-content:center;gap:14px;font:700 44px/1 "Oswald",sans-serif;color:var(--ink)}
  .banner .icon-row{left:32px;top:285px;gap:17px}
  .banner .pest-icon{width:56px;height:56px}
</style>
</head>
<body>

<svg class="sprites" aria-hidden="true">
  <symbol id="bug" viewBox="0 0 24 24">
    <g fill="#111" stroke="#111" stroke-width="1.3" stroke-linecap="round">
      <circle cx="12" cy="5.5" r="2.3" stroke="none"/>
      <ellipse cx="12" cy="10.5" rx="2.4" ry="2.6" stroke="none"/>
      <ellipse cx="12" cy="17" rx="3.4" ry="4.4" stroke="none"/>
      <path d="M10 9 5 6M14 9 19 6M9.8 11.5 4.5 12M14.2 11.5 19.5 12M9.5 14 5 18.5M14.5 14 19 18.5M11 4 9 1.5M13 4 15 1.5" fill="none"/>
    </g>
  </symbol>
  <symbol id="phone" viewBox="0 0 24 24">
    <path fill="currentColor" d="M6.6 2.5 9.4 2l1.8 5-2.2 1.6a12 12 0 0 0 6.4 6.4L17 12.8l5 1.8-.5 2.8c-.3 1.6-1.8 2.8-3.4 2.6C10.6 19 5 13.4 4 5.9 3.8 4.3 5 2.8 6.6 2.5z"/>
  </symbol>
</svg>

<!-- DOOR HANG TAG FRONT -->
<div class="piece-label" style="left:29px;width:272px;top:112px">DOOR HANG TAG FRONT</div>
<section class="piece dark hanger hanger-front">
  <div class="brand">
    <span class="brand-dot"></span>
    <span class="brand-name"><span class="line-main">CITRUS GROVE</span><span class="line-sub">PEST CONTROL</span></span>
  </div>
  <svg class="hanger-hole" width="272" height="95" viewBox="0 0 272 95" aria-hidden="true">
    <path fill="#fff" d="M136 7a40 40 0 0 1 37 25l13 15-13 15a40 40 0 0 1-74 0L86 47l13-15A40 40 0 0 1 136 7z"/>
    <path fill="#fff" d="M0 31 L30 47 L0 63 Z"/>
  </svg>
  <div class="headline"><span class="hl-orange">WE</span> <span class="hl-white">KILL</span><br><span class="hl-orange">BUGS</span></div>
  <div class="photo" role="img" aria-label="Photo of a pest control technician in an orange cap and shirt holding a sprayer wand" style="left:100px;top:386px;width:172px;height:189px;border-radius:60px 0 0 0"></div>
  <div class="callout" style="left:14px;top:262px;width:166px;height:150px;transform:rotate(-5deg)">
    <svg width="166" height="150" viewBox="0 0 166 150" aria-hidden="true">
      <path fill="none" stroke="var(--orange)" stroke-width="5" d="M20 8H5v94h40M144 8h16v94H96L100 140 62 102"/>
    </svg>
    <div class="callout-text" style="top:16px">
      <div class="offer-amount">$50 <small>OFF</small></div>
      <div class="offer-terms" style="margin-top:4px">Initial Home Protection Plan<br>New Customers Only</div>
    </div>
  </div>
  <div class="phone-band" style="top:575px;height:31px"><svg width="16" height="16" style="color:var(--ink)" aria-hidden="true"><use href="#phone"/></svg>555-014-2290</div>
  <div class="cta-band" style="top:606px;height:27px">CALL NOW FOR A FREE QUOTE</div>
</section>

<!-- DOOR HANG TAG BACK -->
<div class="piece-label" style="left:323px;width:272px;top:112px">DOOR HANG TAG BACK</div>
<section class="piece dark hanger hanger-back">
  <div class="brand">
    <span class="brand-dot"></span>
    <span class="brand-name"><span class="line-main">CITRUS GROVE</span><span class="line-sub">PEST CONTROL</span></span>
  </div>
  <svg class="hanger-hole" width="272" height="95" viewBox="0 0 272 95" aria-hidden="true">
    <path fill="#fff" d="M136 7a40 40 0 0 1 37 25l13 15-13 15a40 40 0 0 1-74 0L86 47l13-15A40 40 0 0 1 136 7z"/>
    <path fill="#fff" d="M272 31 L242 47 L272 63 Z"/>
  </svg>
  <div class="about">
    <p>We are a locally owned and operated, with 10 years of industry experience our family is committed to delivering exceptional customer service and high-quality results. We strive for excellence in all that we do.</p>
    <p>We treat each and every customer like a member of our family. When you partner with us, you can enjoy hassle-free services, expert care, and peace of mind knowing you and your home are protected from pests for years to come.</p>
  </div>
  <div class="callout" style="left:40px;top:327px;width:194px;height:170px">
    <svg width="194" height="170" viewBox="0 0 194 170" aria-hidden="true">
      <path fill="none" stroke="var(--orange)" stroke-width="5" d="M12 8H4v118h60M172 3h14v118H100l6 48-48-43"/>
    </svg>
    <div class="callout-text" style="top:20px">
      <div class="offer-amount" style="font-size:62px">$25 <small style="font-size:32px">OFF</small></div>
      <div class="offer-terms" style="font-size:14px;line-height:15px;margin-top:4px">One Time Service<br>New Customers Only</div>
    </div>
  </div>
  <div class="section-title" style="top:511px">OUR SERVICES</div>
  <div class="icon-row" style="left:12px;top:544px;gap:6px">
    <span class="pest-icon" style="width:30px;height:30px"><svg><use href="#bug"/></svg></span>
    <span class="pest-icon" style="width:30px;height:30px"><svg><use href="#bug"/></svg></span>
    <span class="pest-icon" style="width:30px;height:30px"><svg><use href="#bug"/></svg></span>
    <span class="pest-icon is-active" style="width:30px;height:30px"><svg><use href="#bug"/></svg></span>
    <span class="pest-icon" style="width:30px;height:30px"><svg><use href="#bug"/></svg></span>
    <span class="pest-icon" style="width:30px;height:30px"><svg><use href="#bug"/></svg></span>
    <span class="pest-icon" style="width:30px;height:30px"><svg><use href="#bug"/></svg></span>
  </div>
  <div class="web-band" style="left:36px;width:199px;top:593px;height:40px;clip-path:polygon(6px 0,calc(100% - 6px) 0,100% 100%,0 100%)">WWW.CITRUSGROVEPEST.COM</div>
</section>

<!-- SERVICE FLYER -->
<div class="piece-label" style="left:615px;width:556px;top:27px">SERVICE FLYER (letter size)</div>
<section class="piece flyer">
  <div class="brand">
    <span class="brand-dot"></span>
    <span class="brand-name"><span class="line-main">CITRUS GROVE</span><span class="line-sub">PEST CONTROL</span></span>
  </div>
  <div class="flyer-copy">
    <p>Pests are constantly trying to enter your home, which can easily cause frustration and damage to your home and belongings. That's why we at Citrus Grove Pest Control provide seasonally designed, proactive home pest control plans to protect your family and your home.</p>
    <p>Our home pest control plans offer effective and affordable solutions to all your pest issues in and around your home. If you have pest problems, schedule your free inspection today!</p>
    <p><strong>Covered Pests:</strong> Ants, Carpenter Ants, Bees, Carpenter Bees, Box Elder Bugs, Centipedes, Clover Mites, Crickets, General Spiders, Ground Beetles, Earwigs, Millipedes, Mice, Oriental Roaches, Pill Bugs, Sow Bugs, Scorpions, and Wasps all within 10 feet of the structure being treated.</p>
  </div>
  <svg class="tiers" width="556" height="718" viewBox="0 0 556 718" aria-label="Service plan tiers">
    <defs>
      <linearGradient id="shade" x1="0" x2="1"><stop offset="0" stop-color="#000" stop-opacity=".18"/><stop offset=".12" stop-color="#000" stop-opacity="0"/></linearGradient>
    </defs>
    <path fill="var(--bronze)" d="M197 303H512L476 397H197Z"/>
    <path fill="url(#shade)" d="M197 303H512L476 397H197Z"/>
    <path fill="var(--silver)" d="M197 400H512L476 492H197Z"/>
    <path fill="url(#shade)" d="M197 400H512L476 492H197Z"/>
    <path fill="var(--gold)" d="M197 493H512L476 586H197Z"/>
    <path fill="url(#shade)" d="M197 493H512L476 586H197Z"/>
    <path fill="var(--gold-dark)" d="M63 493H197L212 503V600L130 637L63 605Z"/>
    <path fill="var(--gold)" d="M63 505H197V600L130 635L63 605Z"/>
    <path fill="var(--silver-dark)" d="M63 400H197L212 410V510L130 540L63 510Z"/>
    <path fill="var(--silver)" d="M63 410H197V510L130 540L63 510Z"/>
    <path fill="var(--bronze-dark)" d="M63 289H197L212 300V415L130 448L63 415Z"/>
    <path fill="var(--bronze)" d="M63 289H197V415L130 448L63 415Z"/>
    <text class="tier-name" text-anchor="middle"><tspan x="130" y="335">HOME</tspan><tspan x="130" y="355">DEFENSE</tspan><tspan x="130" y="375">BRONZE</tspan></text>
    <text class="tier-name" text-anchor="middle"><tspan x="130" y="472">HOME</tspan><tspan x="130" y="492">DEFENSE</tspan><tspan x="130" y="512">SILVER</tspan></text>
    <text class="tier-name" text-anchor="middle"><tspan x="130" y="569">HOME</tspan><tspan x="130" y="589">DEFENSE</tspan><tspan x="130" y="609">GOLD</tspan></text>
    <g class="tier-feature">
      <text><tspan x="217" y="314">»  Year-Round Pest Protection</tspan><tspan x="217" y="325">»  Bi-Monthly Service (6 visits per year)</tspan><tspan x="217" y="336">»  Covers 15+ Pests</tspan><tspan x="217" y="347">»  Exterior Treatment</tspan><tspan x="217" y="358">»  Interior Treatment (As Needed)</tspan><tspan x="217" y="369">»  Rodent Control</tspan><tspan x="217" y="380">»  Stinging Insect Removal</tspan><tspan x="217" y="391">»  Free Re-Treatments</tspan></text>
      <text><tspan x="217" y="412">»  Year-Round Pest Protection</tspan><tspan x="217" y="423">»  Bi-Monthly Service (6 visits per year)</tspan><tspan x="217" y="434">»  Covers 15+ Pests</tspan><tspan x="217" y="445">»  Exterior Treatment</tspan><tspan x="217" y="456">»  Interior Treatment (As Needed)</tspan><tspan x="217" y="467">»  Rodent Control</tspan><tspan x="217" y="478">»  Stinging Insect Removal</tspan><tspan x="217" y="489">»  Free Re-Treatments</tspan></text>
      <text><tspan x="217" y="509">»  Year-Round Pest Protection</tspan><tspan x="217" y="519">»  Bi-Monthly Service (6 visits per year)</tspan><tspan x="217" y="529">»  Covers 15+ Pests</tspan><tspan x="217" y="539">»  Exterior Treatment</tspan><tspan x="217" y="549">»  Interior Treatment (As Needed)</tspan><tspan x="217" y="559">»  Rodent Control</tspan><tspan x="217" y="569">»  Stinging Insect Removal</tspan><tspan x="217" y="579">»  Free Re-Treatments</tspan></text>
    </g>
    <text class="tier-price" x="360" y="379">$</text><path d="M373 380h56" stroke="#222" stroke-width=".8"/>
    <text class="tier-price" x="360" y="459">$</text><path d="M373 460h56" stroke="#222" stroke-width=".8"/>
    <text class="tier-extra" x="365" y="479">+ Termite Monitoring</text>
    <text class="tier-price" x="360" y="539">$</text><path d="M373 540h56" stroke="#222" stroke-width=".8"/>
    <text class="tier-extra"><tspan x="365" y="558">+ Termite Monitoring &amp;</tspan><tspan x="374" y="568">Mosquito Reduction</tspan><tspan x="374" y="578">Treatments</tspan></text>
  </svg>
  <p class="flyer-note"><strong>Please Note:</strong> to have full guarantee for Asian Beetles, Brown Recluse Spider, Cluster Flies, Lady Bugs, and Silverfish the structures attic and/or crawlspace would need to be treated. There are additional fees for theses services.</p>
</section>

<!-- BUSINESS CARD FRONT -->
<div class="piece-label" style="left:47px;width:254px;top:813px">BUSINESS CARD FRONT</div>
<section class="piece dark card card-front">
  <div class="brand">
    <span class="brand-dot"></span>
    <span class="brand-name"><span class="line-main">CITRUS GROVE</span><span class="line-sub">PEST CONTROL</span></span>
  </div>
  <div class="card-phone"><svg width="10" height="10" style="color:var(--orange)" aria-hidden="true"><use href="#phone"/></svg>555-014-2290</div>
  <div class="card-owner">DAN MERCER, OWNER</div>
  <div class="card-email">DAN@CITRUSGROVEPEST.COM</div>
</section>

<!-- BUSINESS CARD BACK -->
<div class="piece-label" style="left:47px;width:254px;top:1006px">BUSINESS CARD BACK</div>
<section class="piece dark card card-back">
  <div class="card-tab" style="top:0;height:16px;clip-path:polygon(0 0,100% 0,calc(100% - 4px) 100%,4px 100%)">SERVICES / INSPECTIONS</div>
  <div class="brand">
    <span class="brand-dot"></span>
    <span class="brand-name"><span class="line-main">CITRUS GROVE</span><span class="line-sub">PEST CONTROL</span></span>
  </div>
  <div class="icon-row">
    <span class="pest-icon"><svg><use href="#bug"/></svg></span>
    <span class="pest-icon"><svg><use href="#bug"/></svg></span>
    <span class="pest-icon"><svg><use href="#bug"/></svg></span>
    <span class="pest-icon is-active"><svg><use href="#bug"/></svg></span>
    <span class="pest-icon"><svg><use href="#bug"/></svg></span>
    <span class="pest-icon"><svg><use href="#bug"/></svg></span>
    <span class="pest-icon"><svg><use href="#bug"/></svg></span>
  </div>
  <span class="icon-caption" style="left:20px">ANTS</span>
  <span class="icon-caption" style="left:50.5px">MOSQUITOS</span>
  <span class="icon-caption" style="left:81px">ROACHES</span>
  <span class="icon-caption" style="left:111.5px">STINGING<br>INSECTS</span>
  <span class="icon-caption" style="left:142px">SPIDERS</span>
  <span class="icon-caption" style="left:172.5px">RODENTS</span>
  <span class="icon-caption" style="left:203px">TERMITES</span>
  <div class="card-tab" style="top:129px;height:16px;clip-path:polygon(4px 0,calc(100% - 4px) 0,100% 100%,0 100%)">WWW.CITRUSGROVEPEST.COM</div>
</section>

<!-- FACEBOOK BANNER -->
<div class="piece-label" style="left:345px;width:826px;top:788px">FACEBOOK BANNER</div>
<section class="piece dark banner">
  <div class="photo" role="img" aria-label="Photo of a pest control technician in an orange cap, shirt and dark overalls holding a sprayer wand" style="left:420px;top:18px;width:406px;height:345px;border-radius:160px 0 0 0"></div>
  <div class="callout" style="left:462px;top:22px;width:120px;height:120px;transform:rotate(-6deg)">
    <svg width="120" height="120" viewBox="0 0 120 120" aria-hidden="true">
      <path fill="none" stroke="var(--orange)" stroke-width="4" d="M14 6H4v88h44M104 6h12v88H78L86 118 58 94"/>
    </svg>
    <div class="callout-text" style="top:8px;font:700 15px/16px 'Oswald',sans-serif">
      <div style="font-size:38px;line-height:40px">100%</div>Satisfaction<br>Guaranteed
    </div>
  </div>
  <div class="brand">
    <span class="brand-dot"></span>
    <span class="brand-name"><span class="line-main">CITRUS GROVE</span><span class="line-sub" style="color:var(--white)">PEST CONTROL</span></span>
  </div>
  <div class="headline"><span class="hl-orange">WE</span> <span class="hl-white">KILL</span> <span class="hl-orange">BUGS</span></div>
  <div class="banner-phone"><svg width="36" height="36" style="color:var(--ink)" aria-hidden="true"><use href="#phone"/></svg>(555) 014-2290</div>
  <div class="icon-row">
    <span class="pest-icon"><svg><use href="#bug"/></svg></span>
    <span class="pest-icon"><svg><use href="#bug"/></svg></span>
    <span class="pest-icon"><svg><use href="#bug"/></svg></span>
    <span class="pest-icon is-active"><svg><use href="#bug"/></svg></span>
    <span class="pest-icon"><svg><use href="#bug"/></svg></span>
    <span class="pest-icon"><svg><use href="#bug"/></svg></span>
    <span class="pest-icon"><svg><use href="#bug"/></svg></span>
  </div>
</section>

</body>
</html>
```